Payment company requires web design

We need a web design for a new company based in Singapore.

The company focuses on providing 2 key products: 1) an alternative payment option (i.e. like zorbu or plendrixon options) on the traditional checkout process 2) a replacement/outsource of a merchants payment page. Key in the UX flow is a end customer dashboard that manages all payments.

We look to provide a simple, fluid and easy to use payment process. The dashboard is minimalistic that allows easy navigation, review of transactions and all available options through gamification.

The final design should communicate ease of use, flexibility and transparency.

The value is for the merchant - retail/travel/insurance companies. However its the merchant's end customers that are the target and who the UX is built for.

It Company

malvri

5+ page

ec1f27

• 7 pages mimicking UX flow
• payment page * 2 - 1) alternative payment type 2) outsource of merchants payment page to our business
• our landing page
• end customer verification page
• end customer registration
• customer dashboard
• UX flow in attached file
• open to ideas
• have asked for the logo to be added
• logo to have the colour red (chinese for prosperity)
• the company is all about flexibility, transparency in personal finance management with the option of instalment payments

```html
<!DOCTYPE html>
<html lang="en">
<head>
<meta charset="utf-8">
<title>malvri — Dashboard</title>
<link href="https://fonts.googleapis.com/css2?family=Lato:wght@300;400;700&display=swap" rel="stylesheet">
<style>
:root{
  --red:#ec1f27;
  --green:#3f8a1c;
  --ink:#222;
  --muted:#777;
  --line:#e3e3e3;
  --page:#efefef;
  --panel:#fff;
  --dot-off:#d3d3d3;
}
*{box-sizing:border-box;margin:0;padding:0}
html,body{width:1200px;height:854px;overflow:hidden}
body{font-family:'Lato',sans-serif;background:var(--page);color:var(--ink);position:relative}
.sidebar{position:absolute;left:0;top:0;width:194px;height:854px;background:var(--panel)}
.brand{position:absolute;left:50px;top:10px;display:flex;align-items:center;gap:5px;color:var(--red);font-weight:700;font-size:20px}
.brand-mark{width:14px;height:14px;background:var(--red);border-radius:2px}
.avatar-lg{position:absolute;left:62px;top:61px;width:74px;height:74px;border-radius:50%;border:3px solid #f4f4f4;background:radial-gradient(circle at 50% 45%,#c89a80,#3a2a24)}
.user-name{position:absolute;top:145px;width:194px;text-align:center;font-size:14px}
.user-loc{position:absolute;top:165px;width:194px;text-align:center;font-size:10px;color:var(--muted)}
.nav{position:absolute;top:199px;left:0;width:194px;list-style:none}
.nav li{height:37px;display:flex;align-items:center;padding-left:30px;gap:7px;font-size:10.5px;letter-spacing:.4px;border-bottom:1px solid var(--line)}
.nav li.active{background:var(--red);color:#fff;border-bottom:none}
.nav svg{width:10px;height:10px;stroke:currentColor;fill:none;stroke-width:1.4}
.topbar{position:absolute;left:194px;top:0;right:0;height:47px;background:#f7f7f7;border-bottom:1px solid #e2e2e2}
.burger{position:absolute;left:14px;top:19px;width:9px}
.burger span{display:block;height:1.6px;background:#222;margin-bottom:2px}
.gear{position:absolute;left:843px;top:17px}
.user-menu{position:absolute;left:889px;top:11px;display:flex;align-items:center;gap:8px;font-size:10.5px}
.avatar-sm{width:25px;height:25px;border-radius:50%;background:radial-gradient(circle at 50% 45%,#c89a80,#3a2a24)}
.title-band{position:absolute;left:194px;top:48px;right:0;height:68px;background:#f7f7f7}
.page-title{position:absolute;left:12px;top:10px;font-weight:300;font-size:45px;color:#cfcfcf;letter-spacing:.5px}
.search{position:absolute;right:12px;top:20px;width:85px;height:29px;border:1px solid var(--red);border-radius:15px}
.search svg{position:absolute;right:8px;top:8px}
.card{position:absolute;background:var(--panel);border-radius:2px}
.card-title{position:absolute;left:12px;top:17px;font-size:10px;letter-spacing:.3px}
.chev-down{position:absolute;right:12px;top:19px}
.credit{left:206px;top:147px;width:288px;height:285px;overflow:hidden}
.donut{position:absolute;left:64px;top:51px}
.credit-split{position:absolute;left:0;right:0;bottom:0;height:59px;border-top:1px solid var(--line);display:flex}
.credit-cell{flex:1;padding:6px 12px 0}
.credit-cell.limit{border-left:1px solid var(--line);text-align:right}
.big{font-size:26px;font-weight:300;line-height:1.1}
.big.red{color:var(--red)}
.small{font-size:10px;margin-top:2px}
.purchases{left:506px;top:147px;width:437px;height:285px}
.blank-top{left:956px;top:147px;width:237px;height:285px}
.blank-bottom{left:206px;top:445px;width:338px;height:326px}
.repay{left:556px;top:445px;width:637px;height:326px}
.table{position:absolute;left:12px;right:12px}
.row{display:grid;height:38px;align-items:center;border-bottom:1px solid var(--line);font-size:10px;color:#666;font-weight:300}
.row.head{color:var(--ink);font-size:10px;letter-spacing:.3px;height:40px;font-weight:400}
.purchases .row{grid-template-columns:158px 116px 112px 1fr;padding-left:12px}
.repay .row{grid-template-columns:121px 96px 148px 120px 1fr;padding-left:13px}
.pct-red{color:var(--red)}
.pct-green{color:var(--green)}
.arrow{text-align:right;padding-right:10px;color:#333}
.view-all{position:absolute;right:24px;font-size:10.5px;color:var(--red)}
.dots{display:flex;gap:2px}
.dots i{width:9px;height:9px;border-radius:50%;background:var(--dot-off)}
.dots i.r{background:var(--red)}
.dots i.g{background:var(--green)}
.footer{position:absolute;left:206px;right:7px;top:802px;border-top:1px solid #ddd}
.social{position:absolute;left:0;top:19px;display:flex;gap:12px;font-size:9px;color:#444}
.copy{position:absolute;right:0;top:19px;font-size:10.5px;color:#666}
.copy b{color:var(--red);font-weight:400}
</style>
</head>
<body>
<aside class="sidebar">
  <div class="brand"><span class="brand-mark"></span>malvri</div>
  <div class="avatar-lg" role="img" aria-label="Profile photo of Anong Kittirat"></div>
  <div class="user-name">Anong Kittirat</div>
  <div class="user-loc">Novena, Singapore</div>
  <ul class="nav">
    <li class="active"><svg viewBox="0 0 10 10"><path d="M1 5L5 1.5 9 5M2.2 4v4.5h5.6V4"/></svg>DASHBOARD</li>
    <li><svg viewBox="0 0 10 10"><circle cx="5" cy="3.2" r="2"/><path d="M1.2 9.2c.4-2.2 1.9-3.3 3.8-3.3s3.4 1.1 3.8 3.3z"/></svg>PROFILE</li>
    <li><svg viewBox="0 0 10 10"><rect x="1" y="3" width="8" height="6"/><path d="M2.5 3V1.5h5V3M3 6h4"/></svg>REPAYMENTS</li>
    <li><svg viewBox="0 0 10 10"><circle cx="5" cy="5" r="1.6"/><circle cx="5" cy="5" r="3.8" stroke-dasharray="1.5 1"/></svg>SETTINGS</li>
  </ul>
</aside>

<header class="topbar">
  <div class="burger"><span></span><span></span><span></span></div>
  <svg class="gear" width="10" height="10" viewBox="0 0 10 10"><circle cx="5" cy="5" r="3.3" fill="none" stroke="#222" stroke-width="2.2" stroke-dasharray="1.6 1"/><circle cx="5" cy="5" r="2.2" fill="#222"/><circle cx="5" cy="5" r="1" fill="#f7f7f7"/></svg>
  <div class="user-menu"><div class="avatar-sm" role="img" aria-label="Small profile photo"></div>Hi, Anong <svg width="6" height="4" viewBox="0 0 6 4"><path d="M0 0h6L3 3.5z" fill="#222"/></svg></div>
</header>

<div class="title-band">
  <h1 class="page-title">Dashboard</h1>
  <div class="search"><svg width="10" height="10" viewBox="0 0 10 10"><circle cx="4" cy="4" r="3" fill="none" stroke="#ec1f27" stroke-width="1.6"/><path d="M6.2 6.2L9 9" stroke="#ec1f27" stroke-width="1.8"/></svg></div>
</div>

<section class="card credit">
  <div class="card-title">CREDIT STATUS</div>
  <svg class="chev-down" width="7" height="5" viewBox="0 0 7 5"><path d="M.5 1l3 3 3-3" fill="none" stroke="#333" stroke-width="1"/></svg>
  <svg class="donut" width="160" height="160" viewBox="0 0 160 160">
    <circle cx="80" cy="80" r="75" fill="none" stroke="#f0f0f0" stroke-width="1"/>
    <circle cx="80" cy="80" r="75" fill="none" stroke="#ec1f27" stroke-width="5" stroke-dasharray="354 471" transform="rotate(-90 80 80)"/>
    <text x="80" y="96" text-anchor="middle" font-family="Lato,sans-serif" font-weight="300" font-size="42" fill="#cfcfcf">24%</text>
  </svg>
  <div class="credit-split">
    <div class="credit-cell"><p class="big">$600</p><p class="small">Credit Used</p></div>
    <div class="credit-cell limit"><p class="big red">$2500</p><p class="small">Credit Limit</p></div>
  </div>
</section>

<section class="card purchases">
  <div class="card-title">RECENT PURCHASES</div>
  <svg class="chev-down" width="7" height="5" viewBox="0 0 7 5"><path d="M.5 1l3 3 3-3" fill="none" stroke="#333" stroke-width="1"/></svg>
  <div class="table" style="top:51px">
    <div class="row head"><span>MERCHANT</span><span>AMOUNT</span><span>REPAID</span><span></span></div>
    <div class="row"><span>Lorem ipsum dolor</span><span>$175.00</span><span class="pct-red">37%</span><span class="arrow">›</span></div>
    <div class="row"><span>Duis autem veleum</span><span>$208.00</span><span class="pct-red">58%</span><span class="arrow">›</span></div>
    <div class="row"><span>Claritas est etiam</span><span>$126.00</span><span class="pct-green">100%</span><span class="arrow">›</span></div>
    <div class="row"><span>Mirum est notare</span><span>$350.00</span><span class="pct-green">100%</span><span class="arrow">›</span></div>
  </div>
  <div class="view-all" style="top:256px">View All</div>
</section>

<section class="card blank-top"></section>
<section class="card blank-bottom"></section>

<section class="card repay">
  <div class="card-title">REPAYMENTS</div>
  <div class="table" style="top:50px">
    <div class="row head"><span>PAYMENT #</span><span>DATE</span><span>MERCHANT</span><span>AMOUNT</span><span>INSTALLMENTS LEFT</span></div>
    <div class="row"><span>#43</span><span>Dec 08</span><span>Lorem ipsum dolor</span><span>$500</span><span class="dots"><i class="r"></i><i class="r"></i><i class="r"></i><i></i><i></i></span></div>
    <div class="row"><span>#42</span><span>Dec 03</span><span>Lorem ipsum dolor</span><span>$500</span><span class="dots"><i class="r"></i><i class="r"></i><i></i><i></i><i></i></span></div>
    <div class="row"><span>#41</span><span>Nov 28</span><span>Lorem ipsum dolor</span><span>$500</span><span class="dots"><i class="r"></i><i class="r"></i><i class="r"></i><i class="r"></i><i></i></span></div>
    <div class="row"><span>#40</span><span>Nov 15</span><span>Lorem ipsum dolor</span><span>$500</span><span class="dots"><i class="g"></i><i class="g"></i><i class="g"></i><i class="g"></i><i class="g"></i></span></div>
    <div class="row"><span>#39</span><span>Oct 30</span><span>Lorem ipsum dolor</span><span>$500</span><span class="dots"><i class="g"></i><i class="g"></i><i class="g"></i><i class="g"></i><i class="g"></i></span></div>
  </div>
  <div class="view-all" style="top:301px">View All</div>
</section>

<footer class="footer">
  <div class="social"><span>Folio</span><span>Chirpa</span><span>Linkra</span></div>
  <div class="copy">Copyright © <b>malvri</b> 2016</div>
</footer>
</body>
</html>
```